Flyer Template Design

I have attached 4 files. I would like a design template that could be used across these documents so that they have a common look and feel. The content of the documents is tested and should not be changed significantly. The images can be changed. I have also attache our logo for color compatibility.
Updates

Need extra days to review

Target Market(s)

Wealthy Christian donors

Font styles to use
Serif
Sans Serif

```html
<!DOCTYPE html>
<html lang="en">
<head>
<meta charset="utf-8">
<title>The Harvest Trust – Flyer Series</title>
<link href="https://fonts.googleapis.com/css2?family=Merriweather:ital,wght@0,400;0,700;0,900;1,700&family=Open+Sans:ital,wght@0,400;0,700;1,400;1,700&display=swap" rel="stylesheet">
<style>
:root{
  --stage:#3a3a3c;
  --paper:#ffffff;
  --green:#1b4527;
  --green-dark:#163a20;
  --sky:#5cb9ea;
  --tint:#d3eaf7;
  --tint-soft:#eaf5fc;
  --ink:#2c3a44;
  --serif:"Merriweather",Georgia,serif;
  --sans:"Open Sans",Arial,sans-serif;
}
*{box-sizing:border-box;margin:0;padding:0}
html,body{width:1200px;height:443px;overflow:hidden;background:var(--stage)}
.board{position:relative;width:1200px;height:443px}
.flyer{position:absolute;top:24px;width:280px;height:396px;background:var(--paper);overflow:hidden;font-family:var(--sans);color:var(--ink)}
.flyer::before{content:"";position:absolute;left:0;top:0;right:0;height:6px;background:var(--sky)}
.flyer--lap{left:16px}.flyer--commission{left:312px}.flyer--nations{left:608px}.flyer--coming{left:904px}
.abs{position:absolute}
.brand{position:absolute;display:flex;align-items:center;gap:5px}
.brand__mark{width:22px;height:22px;background:var(--sky);flex:none}
.brand__name{font-family:var(--sans);font-weight:700;color:var(--green);font-size:8px;line-height:1.05;border-left:1px solid var(--green);padding-left:5px}
.contact-top{position:absolute;left:150px;top:20px;border-left:1px solid var(--green);padding-left:7px;color:var(--green)}
.contact-top p{font-size:4.6px}
.email{font-family:var(--serif);font-weight:700;font-style:italic;font-size:8.4px;color:var(--green);white-space:nowrap}
.contact-bar{position:absolute;right:0;bottom:0;width:160px;height:44px;background:var(--green-dark);color:#fff;text-align:center;padding-top:9px}
.contact-bar p{font-size:5px}
.contact-bar .email{color:#fff;font-size:8.2px;display:block;margin-top:3px}
.title{font-family:var(--serif);font-weight:900;color:var(--green);line-height:1.12}
.head{font-family:var(--serif);font-weight:900;color:var(--green);font-size:6.2px;text-transform:uppercase;margin-bottom:2px}
.sub{font-family:var(--serif);font-weight:700;color:var(--green);font-size:6px;margin:2px 0}
.body{font-size:3.7px;line-height:1.42;margin-bottom:3px}
.lead{font-family:var(--serif);font-style:italic;font-weight:700;color:var(--green);font-size:4.4px;margin:2px 0}
.callout{font-family:var(--serif);font-weight:700;color:var(--green);font-size:7.6px;text-align:center;line-height:1.2}
.tint{background:linear-gradient(180deg,var(--tint) 0%,var(--tint-soft) 100%)}
.photo{position:absolute}
.photo--stadium{background:linear-gradient(180deg,#0c2a66 0%,#23509a 55%,#c9a35b 100%)}
.photo--runner{background:linear-gradient(135deg,#c46a3e,#3c2a28 60%,#b8b2a6)}
.photo--portraits{background:linear-gradient(90deg,#c59a86,#8c6a52 50%,#c9b8a4)}
.photo--villagers{background:linear-gradient(90deg,#7a5038,#b3533e 50%,#d6b3a0)}
.photo--faces{background:linear-gradient(135deg,#9b6b4e,#c44a3a 45%,#6b7690)}
.photo--group{background:linear-gradient(90deg,#6e83a8,#b89a7c 50%,#e7e2da)}
.photo--sky{background:linear-gradient(90deg,rgba(211,234,247,0) 0%,#8eb2c9 30%,#f1c873 70%,#5f7f8a 100%)}
</style>
</head>
<body>
<main class="board">

<article class="flyer flyer--lap">
  <div class="brand" style="left:12px;top:18px"><span class="brand__mark"></span><span class="brand__name">THE<br>HARVEST<br>TRUST</span></div>
  <div class="contact-top"><p>To learn more, email Daniel Carver at</p><p class="email">dcarver@harvesttrust.org</p></div>
  <div class="abs" style="left:12px;top:62px;width:268px;height:74px;background:linear-gradient(90deg,var(--tint),#eef7fd)"></div>
  <h1 class="abs title" style="left:30px;top:76px;font-size:20px">The<br>Final Lap</h1>
  <div class="photo photo--stadium" role="img" aria-label="Runners in a floodlit stadium at night" style="left:148px;top:62px;width:132px;height:76px"></div>
  <p class="abs body" style="left:8px;top:142px;width:262px">Every four years, the city marathon is run through the streets of the host city. The final lap, though, is always run in the main stadium. At the end of the race, the runners burst into the stadium for the final lap, and the crowd explodes in celebration of a long race well run. For 2000 years, the church has been running a Marathon, racing to fulfill Jesus' command to "make disciples of all nations." But now we're nearly done: we've come into the stadium; we're on the final lap. And the heavenly crowd is standing and cheering!</p>
  <div class="abs tint" style="left:12px;top:172px;width:100px;height:156px;padding:6px 6px">
    <h2 class="head">Sprinting to the finish</h2>
    <p class="body">In his second letter, the Apostle Peter instructs believers to "hasten the coming of the day of God." As the end of the race draws near, he's saying, we should sprint toward the finish line, striving to finish the race as quickly as we can.</p>
    <p class="sub" style="font-size:4.8px">You can be part of the sprint to the finish.</p>
    <p class="body">Partner with the Harvest Trust and finance the missionaries who are taking the gospel for the first time to those last remaining people groups. Your investment will "hasten the coming of the day of God" by accelerating the effort to "make disciples of every nation." In 2018, our partners sent the gospel to 231 people groups in 35 countries.</p>
  </div>
  <div class="abs" style="left:122px;top:172px;width:148px">
    <h2 class="head" style="font-size:5.2px">The finish line</h2>
    <p class="body">Jesus himself defined the finish line when he said, "This gospel of the kingdom will be preached in the whole world as a testimony to all nations, and then the end will come."</p>
    <p class="sub">When will the Race End?</p>
    <p class="lead">Jesus said, when the gospel has been proclaimed to "all nations."</p>
    <p class="body">In the Bible, the word "nations" refers to people groups: groups of people who share a common ethnicity, culture, and language. Amazingly, there are about 12,000 of these "nations" around the world—and Jesus commanded us to make disciples in all of them!</p>
    <p class="body">Today, there are still about 500 people groups around the world have never heard the gospel. Most of these remaining groups are small and located in remote, difficult places. But now that we know who and where they are, by God's grace it is possible for us to engage every one of them with the gospel within the next 3 years.</p>
    <p class="callout" style="font-size:4.6px;margin-top:5px">In other words, after a long race, we're on the final lap!</p>
    <p class="callout" style="margin-top:6px">Join us as we invest to make disciples in "all nations" by 2022.</p>
  </div>
  <div class="photo photo--runner" role="img" aria-label="Sprinter crossing the finish line" style="left:12px;top:332px;width:100px;height:56px"></div>
  <div class="contact-bar" style="width:164px"><p>To learn more, email Daniel Carver at</p><span class="email">dcarver@harvesttrust.org</span></div>
</article>

<article class="flyer flyer--commission">
  <div class="abs tint" style="left:12px;top:18px;width:112px;height:330px"></div>
  <div class="photo photo--portraits" role="img" aria-label="Two portraits of people from unreached groups" style="left:12px;top:18px;width:112px;height:76px"></div>
  <div class="brand" style="left:140px;top:28px"><span class="brand__mark"></span><span class="brand__name">THE<br>HARVEST<br>TRUST</span></div>
  <h1 class="abs title" style="left:140px;top:74px;font-size:17px">Finishing<br>The Great<br>Commission</h1>
  <div class="abs" style="left:18px;top:110px;width:100px">
    <h2 class="head" style="font-size:5.4px">Where do we stand?</h2>
    <p class="body">Today, there are still about 500 people groups who have never heard the gospel. Most of these groups are small and located in remote, difficult places. These remaining "unengaged" people groups have no known believers.</p>
    <p class="body">But now that we know who and where these groups are, by God's grace it is possible that we can engage every one of them with the gospel within the next 3 years.</p>
    <p class="lead" style="margin:4px 0">In other words, we can finish the Great Commission!</p>
    <h2 class="head" style="font-size:5.4px;margin-top:5px">Hastening his coming</h2>
    <p class="body">The Bible says that believers "ought to live holy and godly lives, looking for and hastening the coming of the day of God." It also says that day will not come until the gospel has been preached to "all nations." So how can we hasten the day of his coming? By finishing the work he gave us to do: making disciples in all nations.</p>
    <p class="sub" style="margin-top:4px">You can make that happen.</p>
    <p class="body">Partner with the Harvest Trust and finance the missionaries who are taking the gospel for the first time to those last remaining people groups. Your investment will "hasten the coming of the day of God" by accelerating the effort to "make disciples in every nation." In 2018, our partners helped take the gospel to 231 people groups in 35 countries.</p>
  </div>
  <div class="photo photo--villagers" role="img" aria-label="Three villagers from remote communities" style="left:140px;top:182px;width:128px;height:58px"></div>
  <div class="abs" style="left:140px;top:250px;width:130px">
    <h2 class="head" style="font-size:5.6px">It's about nations</h2>
    <p class="body">In the Bible, the word "nations" refers to people groups: groups of people who share a common ethnicity, culture, and language. So when Jesus said, "Go and make disciples if all nations," He was telling us to take the gospel to every people group on earth. Amazingly, there are about 12,000 of these people groups scattered throughout the world. And the Great Commission commands us to make disciples in every one of them.</p>
    <p class="callout" style="margin-top:5px">Join us as we invest to make disciples in "all nations" by 2022.</p>
  </div>
  <div class="brand" style="left:14px;top:358px"><span class="brand__mark"></span><span class="brand__name">THE<br>HARVEST<br>TRUST</span></div>
  <div class="contact-bar"><p>To learn more, email Daniel Carver at</p><span class="email">dcarver@harvesttrust.org</span></div>
</article>

<article class="flyer flyer--nations">
  <div class="brand" style="left:20px;top:28px"><span class="brand__mark"></span><span class="brand__name">THE<br>HARVEST<br>TRUST</span></div>
  <div class="photo photo--faces" role="img" aria-label="Grid of portraits from many nations" style="left:156px;top:18px;width:112px;height:88px"></div>
  <h1 class="abs title" style="left:20px;top:78px;font-size:16px">GOD'S HEART</h1>
  <p class="abs title" style="left:20px;top:100px;font-size:10px">FOR THE NATIONS</p>
  <div class="abs" style="left:20px;top:122px;width:114px">
    <p class="body">From beginning to end, the Bible reveals God's heart for "the nations." In Genesis, God promises Abraham, "through your offspring all nations on the earth will be blessed."</p>
    <p class="body">The Psalms prophesy that "all the nations you have made will come and worship before you, Lord..."</p>
    <p class="body">In Isaiah, God promises the Messiah, "I will make you a light to the nations, that my salvation may reach to the ends of the earth."</p>
    <p class="body">Daniel sees one "like a son of man" who "was given authority, glory and sovereign power; all nations and peoples of every language worshiped him."</p>
    <p class="body">In Matthew, Jesus commands his apostles to</p>
  </div>
  <div class="abs" style="left:144px;top:122px;width:124px">
    <p class="body">"Go and make disciples of all nations." And he links his return to the completion of that task, saying, "This gospel of the kingdom will be preached in the whole world as a testimony to all nations, and then the end will come."</p>
    <p class="body">In Revelation, John sees a "great multitude that no one could number, from every nation, from all tribes and peoples and languages, standing before the throne..."</p>
    <p class="body">In the Bible, the word "nations" refers to people groups: groups of people who share a common ethnicity, culture and language. Amazingly, there are more than 12,000 of these nations scattered around the world—and God has promised that every one of them will be included in His Kingdom.</p>
  </div>
  <div class="abs" style="left:12px;top:224px;width:268px;height:80px;background:linear-gradient(90deg,var(--tint),#f2f9fd)"></div>
  <h2 class="abs title" style="left:20px;top:230px;font-size:12.5px">FINISHING THE<br>TASK</h2>
  <div class="photo photo--group" role="img" aria-label="Row of people from unreached groups" style="left:20px;top:262px;width:114px;height:38px"></div>
  <div class="abs" style="left:144px;top:230px;width:124px">
    <p class="body">Today, there are still 500 nations who are not yet represented in God's Kingdom. No one has ever proclaimed the gospel to these "unengaged" people groups, and there are no believers among them. For these groups, God's promises have yet to be fulfilled.</p>
    <p class="body">Most of these groups are small and located in remote, difficult places. But because we now know who and where they are, by God's grace it is possible that we can engage every one of them with the gospel within the next 3 years.</p>
  </div>
  <div class="abs" style="left:20px;top:310px;width:250px">
    <p class="sub">You can make that happen.</p>
    <p class="body">Partner with the Harvest Trust and finance the missionaries who are taking the gospel for the first time to those last remaining people groups. Your investment will "hasten the coming of the day of God" by accelerating the effort to make "disciples in every nation." In 2018, our partners helped take the gospel to 231 people groups in 35 countries.</p>
  </div>
  <div class="brand" style="left:14px;top:358px"><span class="brand__mark"></span><span class="brand__name">THE<br>HARVEST<br>TRUST</span></div>
  <div class="contact-bar" style="height:40px"><p>To learn more, email Daniel Carver at</p><span class="email">dcarver@harvesttrust.org</span></div>
</article>

<article class="flyer flyer--coming">
  <div class="brand" style="left:20px;top:30px"><span class="brand__mark"></span><span class="brand__name">THE<br>HARVEST<br>TRUST</span></div>
  <h1 class="abs title" style="left:124px;top:30px;font-size:14px;text-align:center;width:140px">HASTENING HIS<br>COMING</h1>
  <p class="abs body" style="left:20px;top:78px;width:250px">In his second letter, the Apostle Peter asks, what kind of people should believers be? He answers, "We ought to live holy and godly lives, looking for and hastening the coming of the day of God." But how can we do that? How is it possible to hasten the coming of that day?</p>
  <h2 class="abs title" style="left:20px;top:100px;font-size:12px">“AND THEN THE END WILL COME”</h2>
  <p class="abs body" style="left:20px;top:120px;width:250px">When Jesus' disciples asked Him, Tell us, what will be the sign of your coming and of the end of the age? He replied, This gospel of the kingdom will be preached in the whole world as a testimony to all nations, and then the end will come.</p>
  <div class="abs" style="left:0;top:140px;width:280px;height:158px;background:linear-gradient(90deg,var(--tint) 0%,var(--tint) 45%,#eaf5fc 100%)"></div>
  <div class="photo photo--sky" role="img" aria-label="Sunrise breaking through clouds over the horizon" style="left:120px;top:140px;width:160px;height:108px"></div>
  <div class="abs" style="left:20px;top:146px;width:104px">
    <p class="sub" style="font-size:6px;line-height:1.3">When will Jesus return?<br>He said, only after gospel has been preached to “all nations.”</p>
    <p class="body">In the Bible, the word "nations" refers to people groups: groups of people with common ethnicity, culture, and language. Amazingly, there are about 12,000 of these "nations" around the world—and Jesus commanded His church to preach the gospel to all of them! Today, there are still 500 people groups without a single believer. No one has ever gone to these "unengaged" people groups with the gospel. They do not know the name of Jesus.</p>
    <p class="lead" style="font-size:3.9px">After 2000 years, isn't it time that they all heard?</p>
  </div>
  <div class="abs" style="left:20px;top:254px;width:250px">
    <h2 class="head" style="font-size:5.6px">Finishing the task</h2>
    <p class="body">So how can we "hasten the coming of the day of God?" By completing the work Jesus gave us to do! Jesus said He would not return until the gospel is preached to every nation, so that's what we need to do: take the gospel to all the groups that have never once heard it. Fortunately, we now know who these last groups are and where they are located. By God's grace it is possible that we can engage all of them with the gospel within the next 3 years.</p>
  </div>
  <div class="abs" style="left:20px;top:316px;width:250px">
    <p class="sub">YOU CAN MAKE THAT HAPPEN.</p>
    <p class="body">Partner with the Harvest Trust and finance the missionaries who are taking the gospel for the first time to those last remaining people groups. Your investment will "hasten the coming of the day of God" by accelerating the effort to make "disciples in every nation." In 2018, our partners helped take the gospel to 231 people groups in 35 countries.</p>
  </div>
  <div class="brand" style="left:14px;top:358px"><span class="brand__mark"></span><span class="brand__name">THE<br>HARVEST<br>TRUST</span></div>
  <div class="contact-bar" style="height:40px"><p>To learn more, email Daniel Carver at</p><span class="email">dcarver@harvesttrust.org</span></div>
</article>

</main>
</body>
</html>
```